New Business Card Design Project

Updated business card design. I am moving towards more coaching of, for the most part women, who are searching for more in their lives. I am an intuitive healer, homeopath and nutritionist but also an author and motivational speaker. Int the past I have included my photo on the card but that is not essential. My book is called the Brilliance of Saffron - Reclaiming the Shade of Your Spirit so my colours are typically magenta.
Target Market(s)
Women - 35 - 60 considering improving their health. However, I am also a professional speaker with a target audience including corporate and conferences.
Industry/Entity Type
Health And Wellness
Contact Information for Business Card
Lucinda Parvell, ND, CNP, MA
www.lucindaparvell.com
lucinda@lucindaparvell.com
519-362-7015
Facebook, instagram and twitter logos
Look and feel
Each slider illustrates characteristics of the customer's brand and the style your logo design should communicate.

```html
<!DOCTYPE html>
<html lang="en">
<head>
<meta charset="utf-8">
<title>Lucinda Parvell – Business Card</title>
<link rel="stylesheet" href="https://fonts.googleapis.com/css2?family=Lato:wght@400;700&family=Josefin+Sans:wght@300&display=swap">
<style>
  :root {
    --page-bg: #eeeeee;
    --card-white: #ffffff;
    --stripe: rgba(0, 0, 0, 0.025);
    --magenta: #e8237a;
    --ink: #1e1e1e;
    --on-magenta: #ffffff;
    --photo-leaf: #6f8456;
    --photo-brick: #c9a57a;
    --photo-shade: #8a7a62;
  }
  * { margin: 0; padding: 0; box-sizing: border-box; }
  html, body {
    width: 1200px;
    height: 961px;
    overflow: hidden;
    background: var(--page-bg);
  }
  .business-card {
    position: absolute;
    left: 50px;
    top: 150px;
    width: 1100px;
    height: 661px;
    overflow: hidden;
    background-color: var(--card-white);
    background-image: repeating-linear-gradient(135deg, var(--stripe) 0 2px, transparent 2px 9px);
  }
  .portrait-photo {
    position: absolute;
    left: 650px;
    top: 0;
    width: 450px;
    height: 661px;
    background:
      linear-gradient(90deg, var(--card-white) 0%, rgba(255,255,255,0) 28%),
      linear-gradient(90deg, var(--photo-leaf) 0%, var(--photo-shade) 45%, var(--photo-brick) 75%, var(--photo-brick) 100%);
  }
  .client-name {
    position: absolute;
    left: 81px;
    top: 200px;
    font-family: "Josefin Sans", "Lato", sans-serif;
    font-weight: 300;
    font-size: 74px;
    line-height: 1;
    color: var(--ink);
    letter-spacing: 1px;
    white-space: nowrap;
  }
  .tagline {
    position: absolute;
    left: 150px;
    top: 286px;
    font-family: "Lato", sans-serif;
    font-size: 26px;
    line-height: 1;
    color: var(--ink);
    white-space: nowrap;
  }
  .tagline .dot { color: var(--magenta); margin: 0 8px; }
  .credentials {
    position: absolute;
    left: 497px;
    top: 316px;
    font-family: "Lato", sans-serif;
    font-size: 23px;
    line-height: 1;
    color: var(--magenta);
    white-space: nowrap;
  }
  .card-curves {
    position: absolute;
    left: 0;
    top: 0;
    width: 1100px;
    height: 661px;
  }
  .contact-row {
    position: absolute;
    left: 0;
    width: 100%;
    top: 560px;
    display: flex;
    justify-content: center;
    gap: 26px;
    font-family: "Lato", sans-serif;
    font-size: 22px;
    line-height: 1;
    color: var(--on-magenta);
  }
  .contact-item { display: flex; align-items: center; gap: 10px; }
  .contact-item svg { width: 22px; height: 22px; fill: var(--on-magenta); }
  .website {
    position: absolute;
    left: 0;
    width: 100%;
    top: 601px;
    text-align: center;
    font-family: "Lato", sans-serif;
    font-weight: 700;
    font-size: 23px;
    line-height: 1;
    letter-spacing: 5px;
    color: var(--on-magenta);
  }
</style>
</head>
<body>
  <div class="business-card">
    <div class="portrait-photo" role="img" aria-label="Portrait photo of the coach in a white top leaning against a brick wall beside greenery"></div>

    <div class="client-name">Lucinda Parvell</div>
    <div class="tagline"><span class="dot">•</span>vitality maverick<span class="dot">•</span></div>
    <div class="credentials">ND, CNP, MA</div>

    <svg class="card-curves" viewBox="0 0 1100 661" aria-hidden="true">
      <path d="M0 601 Q 560 442 1100 578 L1100 661 L0 661 Z" fill="var(--magenta)"/>
      <path d="M37 573 Q 591 380 1047 573 Q 591 404 37 573 Z" fill="var(--ink)" stroke="var(--ink)" stroke-width="4" stroke-linejoin="round"/>
    </svg>

    <div class="contact-row">
      <span class="contact-item">
        <svg viewBox="0 0 24 24"><path d="M3 9c0-3 4-5 9-5s9 2 9 5v1.5h-4.5V8.5c-1.5-.6-7.5-.6-9 0v2H3zM7 11h10l3 8H4z"/></svg>
        519-362-7015
      </span>
      <span class="contact-item">
        <svg viewBox="0 0 24 24"><path d="M3 5h18v14H3zM4.5 6.5 12 12.5l7.5-6z" fill-rule="evenodd"/></svg>
        lucinda@lucindaparvell.com
      </span>
    </div>
    <div class="website">www.lucindaparvell.com</div>
  </div>
</body>
</html>
```